Freelance business trainer needs a new business card

My business is called Tbrite. I provide training in the workplace on management, coaching and mentoring, and customer service topics for a variety of businesses, colleges and private training providers, and teach on management programs. I need a professional but eye catching business card. Business colours grey and orange. My name Linda Marchbank; Tel 07853 416207; email lmarchbank@tbrite.co.uk; website www.tbrite.co.uk.
Happy to have some sort of logo on front and details on back or all on one side
Target Market(s)
SME businesses and colleges - workshops i run are for adults in the workplace
Industry/Entity Type
Training
Look and feel

```html
<!DOCTYPE html>
<html lang="en">
<head>
<meta charset="utf-8">
<title>Tbrite – Business Card</title>
<link rel="stylesheet" href="https://fonts.googleapis.com/css2?family=Alfa+Slab+One&family=Cousine:ital,wght@1,400;1,700&display=swap">
<style>
  :root {
    --brand-red: #bc3a25;
    --brand-yellow: #fbba16;
    --brand-grey: #6d6e71;
    --ink: #111111;
    --paper: #ffffff;
  }
  * { margin: 0; padding: 0; box-sizing: border-box; }
  html, body {
    width: 1200px;
    height: 1200px;
    overflow: hidden;
    background: var(--paper);
  }
  .canvas {
    position: relative;
    width: 1200px;
    height: 1200px;
    background: var(--paper);
  }
  .card {
    position: absolute;
    left: 108px;
    width: 966px;
    height: 512px;
    background: var(--brand-red);
  }
  .card--front { top: 56px; }
  .card--back { top: 612px; }
  .card__face {
    position: absolute;
    left: 40px;
    right: 40px;
    top: 22px;
    bottom: 21px;
    background: var(--paper);
  }

  /* Brand name lockup */
  .brand {
    position: absolute;
    display: flex;
    align-items: center;
  }
  .brand__dot {
    border-radius: 50%;
    background: var(--brand-yellow);
    flex: none;
  }
  .brand__name {
    font-family: "Alfa Slab One", serif;
    font-weight: 400;
    color: var(--brand-red);
    line-height: 1;
  }
  .brand--large {
    left: 60px;
    top: 70px;
    gap: 40px;
  }
  .brand--large .brand__dot { width: 300px; height: 300px; }
  .brand--large .brand__name { font-size: 130px; }

  .brand--small {
    right: 28px;
    top: 18px;
    gap: 16px;
  }
  .brand--small .brand__dot { width: 120px; height: 120px; }
  .brand--small .brand__name { font-size: 56px; }

  .role {
    position: absolute;
    right: 26px;
    top: 172px;
    width: 320px;
    text-align: center;
    font-family: "Alfa Slab One", serif;
    font-weight: 400;
    font-size: 22px;
    line-height: 29px;
    color: var(--ink);
    text-transform: uppercase;
  }

  .contact {
    position: absolute;
    left: 30px;
    bottom: 10px;
    font-family: "Cousine", monospace;
    font-style: italic;
    font-weight: 400;
    font-size: 36px;
    line-height: 46px;
    color: var(--ink);
    list-style: none;
  }
  .contact__name { font-weight: 700; }
</style>
</head>
<body>
<main class="canvas">
  <section class="card card--front" aria-label="Card front">
    <div class="card__face">
      <div class="brand brand--large">
        <span class="brand__dot" aria-hidden="true"></span>
        <span class="brand__name">Tbrite</span>
      </div>
    </div>
  </section>

  <section class="card card--back" aria-label="Card back">
    <div class="card__face">
      <div class="brand brand--small">
        <span class="brand__dot" aria-hidden="true"></span>
        <span class="brand__name">Tbrite</span>
      </div>
      <p class="role">Freelance Business<br>Trainer</p>
      <ul class="contact">
        <li class="contact__name">Linda Marchbank</li>
        <li>tel: 07853 416207</li>
        <li>email: lmarchbank@tbrite.co.uk</li>
        <li>Website: www.tbrite.co.uk</li>
      </ul>
    </div>
  </section>
</main>
</body>
</html>
```